Home Page and One Inside Page Needed for Engine Modify Site

Website that sells kits to modify and enhance your car engine performance. I don't like direction / design of current site at http://www.brolvatemotors.com.php53-17.ord1-1.sitepreviewhub.com/

I want something modern. Something that shows power and performance.

I need home page and one inside page.

Keep blues and blacks and unfortunately that is their logo we have to work with. But this site needs WOW factor.

YOU DO NOT HAVE PERMISSION TO WORK OR SPEAK TO CLIENT DIRECTLY AND MUST WORK THROUGH ME.

```html
<!DOCTYPE html>
<html lang="en">
<head>
<meta charset="utf-8">
<title>Brolvate Motors — Shop Online</title>
<link rel="stylesheet" href="https://fonts.googleapis.com/css2?family=League+Spartan:wght@300;400;600;700;800&family=Josefin+Sans:wght@300;400&display=swap">
<style>
  :root {
    --header-blue: #123f7a;
    --header-blue-dark: #0d3469;
    --hero-black: #120203;
    --accent: #5b93f5;
    --ink: #111111;
    --white: #ffffff;
    --photo-grey: #a7a6a2;
    --photo-blue: #3e63b8;
  }
  * { box-sizing: border-box; margin: 0; padding: 0; }
  html, body { width: 1200px; height: 900px; overflow: hidden; background: var(--white); }
  body { font-family: "League Spartan", Arial, sans-serif; color: var(--ink); position: relative; }

  .site-header {
    height: 122px;
    background: repeating-linear-gradient(0deg, var(--header-blue) 0 2px, var(--header-blue-dark) 2px 4px);
    border-bottom: 4px solid var(--white);
    box-sizing: content-box;
    position: relative;
  }
  .brand {
    position: absolute; left: 156px; top: 44px;
    font-size: 37px; font-weight: 400; letter-spacing: 0.6px;
    color: var(--white); text-transform: uppercase; line-height: 1;
  }
  .main-nav { position: absolute; right: 158px; top: 55px; display: flex; gap: 12px; }
  .main-nav a {
    color: var(--white); text-decoration: none; font-weight: 700;
    font-size: 13px; letter-spacing: 0.1px; text-transform: uppercase;
  }

  .hero {
    height: 256px; background: var(--hero-black);
    display: flex; flex-direction: column; align-items: center; justify-content: center;
    border-bottom: 3px solid #e9e9e9;
  }
  .hero-title {
    font-weight: 800; font-size: 86px; color: var(--accent);
    text-transform: uppercase; line-height: 1; letter-spacing: 1.5px; margin-top: 14px;
  }
  .hero-subtitle {
    font-family: "Josefin Sans", Arial, sans-serif; font-weight: 300;
    font-size: 29px; color: var(--white); text-transform: uppercase; margin-top: 4px; letter-spacing: 0;
  }

  .section-title {
    font-weight: 700; font-size: 19px; color: var(--accent); text-transform: uppercase;
    height: 44px; padding-top: 14px; border-bottom: 3px solid var(--accent);
  }

  .catalog { position: absolute; left: 145px; top: 420px; width: 650px; }
  .product-grid {
    margin-top: 20px; display: grid;
    grid-template-columns: repeat(3, 209px); column-gap: 11px; row-gap: 9px;
  }
  .product-card {
    height: 300px; border: 1px solid var(--accent);
    padding: 9px 9px 0; text-align: center;
  }
  .product-photo {
    width: 189px; height: 189px;
    background: radial-gradient(circle at 45% 55%, var(--photo-blue) 0 30%, #8b97b8 45%, var(--photo-grey) 70%);
  }
  .product-name { font-weight: 600; font-size: 19px; color: var(--accent); margin-top: 13px; line-height: 1; }
  .product-price { font-size: 15px; margin-top: 11px; line-height: 1; }
  .add-button {
    display: inline-block; width: 120px; height: 26px; line-height: 28px;
    background: var(--accent); color: var(--white); border-radius: 8px;
    font-weight: 700; font-size: 12px; text-transform: uppercase; margin-top: 10px;
  }

  .cart { position: absolute; left: 820px; top: 420px; width: 234px; }
  .cart-item {
    position: relative; height: 78px; border: 1px solid var(--accent);
    padding: 12px 13px; margin-top: 21px;
  }
  .cart-item + .cart-item { margin-top: 10px; }
  .cart-item-name { font-weight: 600; font-size: 15px; color: var(--accent); line-height: 1; }
  .cart-item-each { font-size: 12px; margin-top: 9px; line-height: 1; }
  .cart-qty {
    position: absolute; right: 8px; top: 10px; width: 47px; height: 26px; line-height: 28px;
    background: var(--accent); color: var(--white); border-radius: 8px;
    text-align: center; font-weight: 700; font-size: 14px;
  }
  .cart-subtotal { position: absolute; right: 9px; bottom: 9px; font-size: 15px; }
  .small-label { font-size: 10px; text-transform: uppercase; letter-spacing: 0.5px; margin-right: 4px; }
  .cart-total {
    margin-top: 10px; height: 48px; border-top: 3px solid var(--accent); border-bottom: 3px solid var(--accent);
    display: flex; align-items: center; justify-content: flex-end; padding-right: 4px;
  }
  .cart-total strong { font-size: 19px; font-weight: 700; }
  .checkout-button {
    display: block; margin-top: 11px; height: 41px; line-height: 44px;
    background: var(--accent); color: var(--white); border-radius: 9px;
    text-align: center; font-weight: 700; font-size: 17px; text-transform: uppercase;
  }
</style>
</head>
<body>
  <header class="site-header">
    <div class="brand">Brolvatemotors</div>
    <nav class="main-nav">
      <a href="#">Home</a><a href="#">Contact Us</a><a href="#">How It Works</a>
      <a href="#">Product</a><a href="#">Resources</a><a href="#">About</a>
    </nav>
  </header>

  <section class="hero">
    <h1 class="hero-title">Shop Online</h1>
    <p class="hero-subtitle">Some Other Subheader</p>
  </section>

  <main class="catalog">
    <h2 class="section-title">4870 Series</h2>
    <div class="product-grid">
      <article class="product-card">
        <div class="product-photo" role="img" aria-label="Product photo: bag of blue header modeling parts"></div>
        <h3 class="product-name">4870B02-00</h3>
        <p class="product-price">$999.99</p>
        <span class="add-button">Add to Cart</span>
      </article>
      <article class="product-card">
        <div class="product-photo" role="img" aria-label="Product photo: bag of blue header modeling parts"></div>
        <h3 class="product-name">4870B02-00</h3>
        <p class="product-price">$999.99</p>
        <span class="add-button">Add to Cart</span>
      </article>
      <article class="product-card">
        <div class="product-photo" role="img" aria-label="Product photo: bag of blue header modeling parts"></div>
        <h3 class="product-name">4870B02-00</h3>
        <p class="product-price">$999.99</p>
        <span class="add-button">Add to Cart</span>
      </article>
      <article class="product-card">
        <div class="product-photo" role="img" aria-label="Product photo: bag of blue header modeling parts"></div>
      </article>
      <article class="product-card">
        <div class="product-photo" role="img" aria-label="Product photo: bag of blue header modeling parts"></div>
      </article>
      <article class="product-card">
        <div class="product-photo" role="img" aria-label="Product photo: bag of blue header modeling parts"></div>
      </article>
    </div>
  </main>

  <aside class="cart">
    <h2 class="section-title">Your Cart</h2>
    <div class="cart-item">
      <div class="cart-item-name">4870B02-00</div>
      <div class="cart-item-each">$999.99 <span class="small-label">each</span></div>
      <span class="cart-qty">X 4</span>
      <div class="cart-subtotal"><span class="small-label">subtotal</span>$3999.96</div>
    </div>
    <div class="cart-item">
      <div class="cart-item-name">4870B02-00</div>
      <div class="cart-item-each">$999.99 <span class="small-label">each</span></div>
      <span class="cart-qty">X 4</span>
      <div class="cart-subtotal"><span class="small-label">subtotal</span>$3999.96</div>
    </div>
    <div class="cart-total"><span class="small-label">current total</span><strong>$7999.92</strong></div>
    <span class="checkout-button">Proceed to Checkout</span>
  </aside>
</body>
</html>
```